BRELM - Letterhead

Willowmere Institute of Letters and Crafts (BRELM) is a non-profit organization that operates two tuition-free public schools - BRELM Elementary for grades K to 5th and BRELM College Prep for grades 6-12.

We are looking for a letterhead primarily to be used on Google Docs and Microsoft Word. Attached are two versions of our logo. One with our name spelled out and one with the acronym.

For Letterhead, we would like 3 addresses listed:

BRELM HQ
41872 Hollow Brook Lane, Suite 308
Fernbrook Hills, CA 94012

BRELM Elementary (K-5)
18460 Marsh Ridge Boulevard
Fernbrook Hills, CA 94012

BRELM College Prep (6-12)
27314 Del Sol Terrace
Larkspur Bay, CA 94038

Our Phone Number is (555) 418-7062
Our Fax Number is the same (555) 418-7062

Our website is www.brelmschools.org

Target Market(s)

Education

Industry/Entity Type

Education

Font styles to use
Sans Serif

Colors
0054AA
0677BA
7BADD7
CADEEF
E8F1F8

Requirements
Must have
• Logo, Address, Phone Number, Website.
Nice to have
• Modern and clean design.
Should not have
• Prefer that there is no bleed -- the letterhead will mostly be used in PDF format however sometimes it will be printed and our printers can not do a full bleed

```html
<!DOCTYPE html>
<html lang="en">
<head>
<meta charset="utf-8">
<title>BRELM Letterhead – Two Samples</title>
<link rel="stylesheet" href="https://fonts.googleapis.com/css2?family=Figtree:ital,wght@0,400;0,500;0,600;0,700;0,800;1,400&display=swap">
<style>
  :root {
    --stage: #808080;
    --label: #a9a9a9;
    --paper: #ffffff;
    --ink: #1f1f1f;
    --navy: #0a35a0;
    --title: #1b3f9c;
    --sky: #0a84d0;
    --green: #12a03a;
    --orange: #ff5a36;
    --red: #f20d0d;
    --yellow: #f2cd00;
    --sig: #e8f1f8;
  }
  * { box-sizing: border-box; margin: 0; padding: 0; }
  html, body { width: 1200px; height: 802px; overflow: hidden; }
  body { background: var(--stage); font-family: "Figtree", Arial, sans-serif; color: var(--ink); position: relative; }

  .sample-label {
    position: absolute; top: 138px; font-size: 13px; letter-spacing: .5px;
    color: var(--label); transform: rotate(-90deg); transform-origin: left top; white-space: nowrap;
  }

  .sheet {
    position: absolute; top: 80px; width: 468px; height: 662px; background: var(--paper);
    overflow: hidden; box-shadow: 0 2px 6px rgba(0,0,0,.25);
  }
  .sheet--one { left: 92px; }
  .sheet--two { left: 648px; }

  .side-stripe { position: absolute; left: 0; top: 0; width: 15px; height: 100%; display: flex; flex-direction: column; }
  .side-stripe span { flex: 1; }

  .brand { position: absolute; display: flex; align-items: center; gap: 12px; }
  .brand-mark { width: 58px; height: 58px; background: var(--navy); flex: none; }
  .brand-name { font-weight: 800; font-size: 21px; line-height: 25px; color: var(--title); text-align: center; letter-spacing: -.2px; }
  .sheet--one .brand { left: 100px; top: 38px; }
  .sheet--two .brand { left: 100px; top: 22px; }

  .rule { position: absolute; left: 34px; top: 114px; width: 403px; height: 2px; display: flex; }
  .rule span { flex: 1; }

  .sender { position: absolute; }
  .person-name { font-weight: 700; font-size: 11px; line-height: 12px; }
  .person-role { font-style: italic; font-size: 7.5px; line-height: 9px; }

  .letter-body { position: absolute; top: 212px; width: 376px; font-size: 7.25px; line-height: 9.4px; text-align: justify; }
  .letter-body p + p { margin-top: 9.4px; }

  .signature { position: absolute; top: 471px; width: 94px; height: 44px; background: var(--sig); border-radius: 3px; }

  .sheet--one .sender--top { left: 52px; top: 168px; }
  .sheet--one .letter-body { left: 50px; }
  .sheet--one .signature { left: 50px; }
  .sheet--one .sender--bottom { left: 52px; top: 521px; }

  .sheet--two .sender--top { left: 49px; top: 168px; }
  .sheet--two .letter-body { left: 49px; }
  .sheet--two .signature { left: 52px; }
  .sheet--two .sender--bottom { left: 53px; top: 521px; }

  /* sample one footer */
  .campus { position: absolute; top: 597px; display: flex; gap: 8px; font-size: 6.4px; line-height: 8.2px; }
  .campus svg { width: 10px; height: 11px; flex: none; }
  .campus-name { font-weight: 600; font-size: 6.6px; }
  .campus--hq { left: 49px; } .campus--hq .campus-name { color: var(--red); }
  .campus--elem { left: 183px; } .campus--elem .campus-name { color: var(--sky); }
  .campus--prep { left: 311px; } .campus--prep .campus-name { color: var(--navy); }

  .contact-row { position: absolute; top: 633px; left: 50px; width: 378px; display: flex; justify-content: space-between; font-size: 8px; }
  .contact-item { display: flex; align-items: center; gap: 7px; white-space: nowrap; }
  .contact-item svg { width: 8px; height: 8px; }

  /* sample two footer */
  .footer-title { position: absolute; left: 30px; top: 597px; font-weight: 700; font-size: 9.5px; color: var(--title); letter-spacing: -.1px; }
  .contact-grid { position: absolute; left: 30px; top: 614px; display: grid; grid-template-columns: 118px auto; row-gap: 3px; font-size: 8px; line-height: 10px; }

  .base-band { position: absolute; left: 0; bottom: 0; width: 296px; height: 10px; display: flex; }
  .base-band span { flex: 1; }

  .campus-panel {
    position: absolute; display: flex; flex-direction: column; align-items: center; justify-content: center;
    text-align: center; font-size: 5.4px; line-height: 6.6px; color: #fff; padding: 4px;
  }
  .campus-panel strong { font-weight: 700; font-size: 5.8px; display: block; }
  .campus-panel svg { display: block; margin-bottom: 4px; width: 7px; height: 9px; }
  .campus-panel--hq { left: 344px; top: 522px; width: 84px; height: 68px; background: var(--yellow); color: var(--ink); }
  .campus-panel--accent { left: 432px; top: 522px; width: 36px; height: 68px; background: var(--orange); }
  .campus-panel--elem { left: 300px; top: 594px; width: 82px; height: 68px; background: var(--green); }
  .campus-panel--prep { left: 386px; top: 594px; width: 82px; height: 68px; background: var(--sky); }
</style>
</head>
<body>

<div class="sample-label" style="left:60px">SAMPLE 1</div>
<div class="sample-label" style="left:613px">SAMPLE 2</div>

<!-- Sample one -->
<section class="sheet sheet--one">
  <div class="side-stripe">
    <span style="background:var(--navy)"></span><span style="background:var(--sky)"></span>
    <span style="background:var(--green)"></span><span style="background:var(--orange)"></span>
    <span style="background:var(--red)"></span><span style="background:var(--yellow)"></span>
  </div>

  <div class="brand">
    <div class="brand-mark"></div>
    <div class="brand-name">Willowmere Institute<br>of Letters and Crafts</div>
  </div>

  <div class="sender sender--top">
    <div class="person-name">Name Goes Here</div>
    <div class="person-role">Designation here</div>
  </div>

  <div class="letter-body">
    <p>Lorem Ipsum is simply dummy text of the printing and typesetting industry. Lorem Ipsum has been the industry's standard dummy text ever since the 1500s, when an unknown printer took a galley of type and scrambled it to make a type specimen book. It has survived not only five centuries, but also the leap into electronic typesetting, remaining essentially unchanged. It was popularised in the 1960s with the release of Letraset sheets containing Lorem Ipsum passages, and more recently with desktop publishing software like Aldus PageMaker including versions of Lorem Ipsum. Lorem Ipsum is simply dummy text of the printing and typesetting industry. Lorem Ipsum has been the industry's standard dummy text ever since the 1500s, when an unknown printer took a galley of type and scrambled it to make a type specimen book.</p>
    <p>Lorem Ipsum is simply dummy text of the printing and typesetting industry. Lorem Ipsum has been the industry's standard dummy text ever since the 1500s, when an unknown printer took a galley of type and scrambled it to make a type specimen book. It has survived not only five centuries, but also the leap into electronic typesetting, remaining essentially unchanged. It was popularised in the 1960s with the release of Letraset sheets containing Lorem Ipsum passages, and more recently with desktop publishing software like Aldus PageMaker including versions of Lorem Ipsum. Lorem Ipsum is simply dummy text of the printing and typesetting industry. Lorem Ipsum has been the industry's standard dummy text ever since the 1500s, when an unknown printer took a galley of type and scrambled it to make a type specimen book.</p>
    <p>Lorem Ipsum is simply dummy text of the printing and typesetting industry. Lorem Ipsum has been the industry's standard dummy text ever since the 1500s, when an unknown printer took a galley of type and scrambled it to make a type specimen book. It has survived not only five centuries, but also the leap into electronic typesetting, remaining essentially unchanged. It was popularised in the 1960s with the release of Letraset sheets containing Lorem Ipsum passages, and more recently with desktop publishing software like Aldus PageMaker including versions of Lorem Ipsum.</p>
  </div>

  <div class="signature" role="img" aria-label="Handwritten signature"></div>
  <div class="sender sender--bottom">
    <div class="person-name">Name Goes Here</div>
    <div class="person-role">Designation here</div>
  </div>

  <div class="campus campus--hq">
    <svg viewBox="0 0 10 11"><path d="M5 0 9.5 2.6v5.8L5 11 .5 8.4V2.6Z" fill="var(--red)"/><circle cx="5" cy="5" r="1.7" fill="#fff"/></svg>
    <div><div class="campus-name">BRELM HQ</div>41872 Hollow Brook Lane, Suite 308<br>Fernbrook Hills, CA 94012</div>
  </div>
  <div class="campus campus--elem">
    <svg viewBox="0 0 10 11"><path d="M5 0 9.5 2.6v5.8L5 11 .5 8.4V2.6Z" fill="var(--sky)"/><circle cx="5" cy="5" r="1.7" fill="#fff"/></svg>
    <div><div class="campus-name">BRELM Elementary (K-5)</div>18460 Marsh Ridge Boulevard<br>Fernbrook Hills, CA 94012</div>
  </div>
  <div class="campus campus--prep">
    <svg viewBox="0 0 10 11"><path d="M5 0 9.5 2.6v5.8L5 11 .5 8.4V2.6Z" fill="var(--navy)"/><circle cx="5" cy="5" r="1.7" fill="#fff"/></svg>
    <div><div class="campus-name">BRELM College Prep (6-12)</div>27314 Del Sol Terrace<br>Larkspur Bay, CA 94038</div>
  </div>

  <div class="contact-row">
    <div class="contact-item"><svg viewBox="0 0 8 8"><path d="M1.5 .5 3 2 2.2 3.1a5 5 0 0 0 2.7 2.7L6 5l1.5 1.5L6.6 7.5C3.5 7.3.7 4.5.5 1.4Z" fill="var(--sky)"/></svg>(555) 418-7062</div>
    <div class="contact-item"><svg viewBox="0 0 8 8"><rect x="2" y=".5" width="4" height="2" fill="none" stroke="var(--sky)"/><rect x=".5" y="2.5" width="7" height="3.5" fill="none" stroke="var(--sky)"/><rect x="2" y="5" width="4" height="2.5" fill="none" stroke="var(--sky)"/></svg>(555) 418-7062</div>
    <div class="contact-item"><svg viewBox="0 0 8 8"><rect x=".5" y="1.5" width="7" height="5" fill="var(--sky)"/><path d="M.5 1.5 4 4.5l3.5-3" fill="none" stroke="#fff" stroke-width=".8"/></svg>admissions@brelmschools.org</div>
    <div class="contact-item"><svg viewBox="0 0 8 8"><circle cx="4" cy="4" r="3.4" fill="none" stroke="var(--sky)" stroke-width=".8"/><ellipse cx="4" cy="4" rx="1.4" ry="3.4" fill="none" stroke="var(--sky)" stroke-width=".6"/><path d="M.6 4h6.8" stroke="var(--sky)" stroke-width=".6"/></svg>www.brelmschools.org</div>
  </div>
</section>

<!-- Sample two -->
<section class="sheet sheet--two">
  <div class="brand">
    <div class="brand-mark"></div>
    <div class="brand-name">Willowmere Institute<br>of Letters and Crafts</div>
  </div>
  <div class="rule">
    <span style="background:var(--yellow)"></span><span style="background:var(--red)"></span>
    <span style="background:var(--orange)"></span><span style="background:var(--green)"></span>
    <span style="background:var(--sky)"></span><span style="background:var(--navy)"></span>
  </div>

  <div class="sender sender--top">
    <div class="person-name">Name Goes Here</div>
    <div class="person-role">Designation here</div>
  </div>

  <div class="letter-body">
    <p>Lorem Ipsum is simply dummy text of the printing and typesetting industry. Lorem Ipsum has been the industry's standard dummy text ever since the 1500s, when an unknown printer took a galley of type and scrambled it to make a type specimen book. It has survived not only five centuries, but also the leap into electronic typesetting, remaining essentially unchanged. It was popularised in the 1960s with the release of Letraset sheets containing Lorem Ipsum passages, and more recently with desktop publishing software like Aldus PageMaker including versions of Lorem Ipsum. Lorem Ipsum is simply dummy text of the printing and typesetting industry. Lorem Ipsum has been the industry's standard dummy text ever since the 1500s, when an unknown printer took a galley of type and scrambled it to make a type specimen book.</p>
    <p>Lorem Ipsum is simply dummy text of the printing and typesetting industry. Lorem Ipsum has been the industry's standard dummy text ever since the 1500s, when an unknown printer took a galley of type and scrambled it to make a type specimen book. It has survived not only five centuries, but also the leap into electronic typesetting, remaining essentially unchanged. It was popularised in the 1960s with the release of Letraset sheets containing Lorem Ipsum passages, and more recently with desktop publishing software like Aldus PageMaker including versions of Lorem Ipsum. Lorem Ipsum is simply dummy text of the printing and typesetting industry. Lorem Ipsum has been the industry's standard dummy text ever since the 1500s, when an unknown printer took a galley of type and scrambled it to make a type specimen book.</p>
    <p>Lorem Ipsum is simply dummy text of the printing and typesetting industry. Lorem Ipsum has been the industry's standard dummy text ever since the 1500s, when an unknown printer took a galley of type and scrambled it to make a type specimen book. It has survived not only five centuries, but also the leap into electronic typesetting, remaining essentially unchanged. It was popularised in the 1960s with the release of Letraset sheets containing Lorem Ipsum passages, and more recently with desktop publishing software like Aldus PageMaker including versions of Lorem Ipsum.</p>
  </div>

  <div class="signature" role="img" aria-label="Handwritten signature"></div>
  <div class="sender sender--bottom">
    <div class="person-name">Name Goes Here</div>
    <div class="person-role">Designation here</div>
  </div>

  <div class="footer-title">Willowmere Institute of Letters and Crafts</div>
  <div class="contact-grid">
    <div class="contact-item"><svg viewBox="0 0 8 8"><path d="M1.5 .5 3 2 2.2 3.1a5 5 0 0 0 2.7 2.7L6 5l1.5 1.5L6.6 7.5C3.5 7.3.7 4.5.5 1.4Z" fill="var(--sky)"/></svg>Phone: (555) 418-7062</div>
    <div class="contact-item"><svg viewBox="0 0 8 8"><rect x=".5" y="1.5" width="7" height="5" fill="var(--sky)"/><path d="M.5 1.5 4 4.5l3.5-3" fill="none" stroke="#fff" stroke-width=".8"/></svg>Email: admissions@brelmschools.org</div>
    <div class="contact-item"><svg viewBox="0 0 8 8"><rect x="2" y=".5" width="4" height="2" fill="none" stroke="var(--sky)"/><rect x=".5" y="2.5" width="7" height="3.5" fill="none" stroke="var(--sky)"/><rect x="2" y="5" width="4" height="2.5" fill="none" stroke="var(--sky)"/></svg>Fax: (555) 418-7062</div>
    <div class="contact-item"><svg viewBox="0 0 8 8"><circle cx="4" cy="4" r="3.4" fill="none" stroke="var(--sky)" stroke-width=".8"/><ellipse cx="4" cy="4" rx="1.4" ry="3.4" fill="none" stroke="var(--sky)" stroke-width=".6"/><path d="M.6 4h6.8" stroke="var(--sky)" stroke-width=".6"/></svg>Visit: www.brelmschools.org</div>
  </div>

  <div class="base-band">
    <span style="background:var(--yellow)"></span><span style="background:var(--red)"></span>
    <span style="background:var(--orange)"></span><span style="background:var(--green)"></span>
    <span style="background:var(--sky)"></span><span style="background:var(--navy)"></span>
  </div>

  <div class="campus-panel campus-panel--hq">
    <svg viewBox="0 0 7 9"><path d="M3.5 9S.3 5.4.3 3.3a3.2 3.2 0 0 1 6.4 0C6.7 5.4 3.5 9 3.5 9Z" fill="#fff"/><circle cx="3.5" cy="3.3" r="1.2" fill="var(--yellow)"/></svg>
    <strong>BRELM HQ</strong>41872 Hollow Brook Lane,<br>Suite 308,<br>Fernbrook Hills,<br>CA 94012
  </div>
  <div class="campus-panel campus-panel--accent"></div>
  <div class="campus-panel campus-panel--elem">
    <svg viewBox="0 0 7 9"><path d="M3.5 9S.3 5.4.3 3.3a3.2 3.2 0 0 1 6.4 0C6.7 5.4 3.5 9 3.5 9Z" fill="#fff"/><circle cx="3.5" cy="3.3" r="1.2" fill="var(--green)"/></svg>
    <strong>BRELM<br>Elementary (K-5)</strong>18460 Marsh Ridge Blvd<br>Fernbrook Hills, CA 94012
  </div>
  <div class="campus-panel campus-panel--prep">
    <svg viewBox="0 0 7 9"><path d="M3.5 9S.3 5.4.3 3.3a3.2 3.2 0 0 1 6.4 0C6.7 5.4 3.5 9 3.5 9Z" fill="#fff"/><circle cx="3.5" cy="3.3" r="1.2" fill="var(--sky)"/></svg>
    <strong>BRELM College<br>Prep (6-12)</strong>27314 Del Sol Terrace<br>Larkspur Bay,<br>CA 94038
  </div>
</section>

</body>
</html>
```